Radiant Harvest Gathering 2021

I am looking to create a flyer for a one day prayer retreat our church is organizing. This flyer will be posted on social media, websites, mobile apps, and will also be printed so it can be mailed to people.

I am looking for something professional, with good use of our logo and band colors (logo colors).

I am counting on the designer's skill, creativity, art and knowledge of media communication to produce a flyer that will effectively and quickly convey the message we are trying to spread.

CONTENT OF THE FLYER:
Event title: Radiant Harvest Gathering
Date: Tuesday July 2nd, 2021
Time: 11:00AM - 7:00PM
Bellmore Hotel, 4817 Wexley Avenue, Portland, Maine 04109 (Room: Tamarind)
Event Key words to highlight what the event is about: Prayer, Fasting, Worship, Prophecy, Revival.
Key phrases:
A one day prayer retreat.
Jesus Chris is Lord

Contact info:
www.quvello.org
Phone: 207 555 0148
Email: contact@brookmeadow.org

```html
<!DOCTYPE html>
<html lang="en">
<head>
<meta charset="utf-8">
<title>Radiant Harvest Gathering 2021</title>
<link rel="stylesheet" href="https://fonts.googleapis.com/css2?family=Alfa+Slab+One&family=Montserrat:wght@600;700&family=Oranienbaum&family=Cormorant+SC:wght@600&display=swap">
<style>
  :root {
    --page: #f2f3f4;
    --paper: #ffffff;
    --navy: #1f3a63;
    --ink: #1c1c1c;
    --red: #c3202b;
    --violet: #8a5db0;
    --blue: #1d4f9c;
    --steel: #5b6f9a;
    --logo-navy: #12355e;
  }
  * { box-sizing: border-box; margin: 0; padding: 0; }
  html, body { width: 1199px; height: 1200px; overflow: hidden; background: var(--page); }
  .flyer {
    position: absolute; left: 166px; top: 40px;
    width: 866px; height: 1120px;
    background: var(--paper); overflow: hidden;
  }
  .hero {
    position: absolute; left: 0; top: 0; width: 866px; height: 700px;
    background:
      linear-gradient(180deg, rgba(255,255,255,0) 62%, #fff 96%),
      radial-gradient(ellipse 38% 60% at 50% 55%, #a9b3d0 0%, rgba(169,179,208,0) 70%),
      linear-gradient(90deg, #6a4a38 0%, #b78658 30%, #e9c19a 50%, #b59a86 72%, #5f7890 100%),
      linear-gradient(180deg, #f6e3d2 0%, #c58c5e 40%, #8e6b55 100%);
    background-blend-mode: normal, normal, multiply, normal;
  }
  .streaks { position: absolute; left: 0; top: 0; }
  .keywords {
    position: absolute; top: 46px; left: 0; width: 100%;
    text-align: center; font-family: "Oranienbaum", serif;
    font-size: 27px; letter-spacing: 0.5px; color: var(--ink);
  }
  .badge {
    position: absolute; left: 605px; top: 124px; width: 206px; height: 206px;
    border-radius: 50%; background: var(--logo-navy);
    border: 6px solid #fff; box-shadow: 0 0 0 3px var(--logo-navy);
    display: flex; align-items: center; justify-content: center;
  }
  .badge-name {
    font-family: "Montserrat", sans-serif; font-weight: 700;
    font-size: 30px; color: #fff; letter-spacing: 1px;
  }
  .title {
    position: absolute; left: 0; width: 100%; top: 605px; text-align: center;
    font-family: "Alfa Slab One", serif; line-height: 1;
  }
  .title span {
    display: block;
    background: linear-gradient(90deg, var(--violet) 0%, var(--blue) 45%, var(--steel) 100%);
    -webkit-background-clip: text; background-clip: text; color: transparent;
  }
  .title .line-one { font-size: 66px; }
  .title .line-two { font-size: 92px; margin-top: 2px; }
  .rule {
    position: absolute; left: 80px; width: 706px; height: 3px;
    background: linear-gradient(90deg, rgba(31,58,99,0), var(--navy) 15%, var(--navy) 85%, rgba(31,58,99,0));
  }
  .details {
    position: absolute; left: 0; width: 100%; top: 838px; text-align: center;
    font-family: "Montserrat", sans-serif; font-weight: 600; color: var(--navy);
  }
  .details .date, .details .time { font-size: 30px; line-height: 52px; }
  .details .venue { font-size: 23px; line-height: 34px; margin-top: 6px; }
  .details .room { font-size: 23px; line-height: 34px; }
  .details .room b { color: var(--red); font-weight: 600; }
  .tagline {
    position: absolute; left: 0; width: 100%; top: 1048px; text-align: center;
    font-family: "Cormorant SC", serif; font-weight: 600; font-size: 30px; color: var(--ink);
  }
</style>
</head>
<body>
  <main class="flyer">
    <div class="hero" role="img" aria-label="Photo of a man in a checked shirt praying with bowed head, city skyline glowing at dusk behind him"></div>
    <svg class="streaks" width="866" height="700" viewBox="0 0 866 700" aria-hidden="true">
      <line x1="30" y1="0" x2="250" y2="420" stroke="#fff" stroke-width="3" opacity="0.7"/>
      <line x1="770" y1="10" x2="866" y2="170" stroke="#1c2a40" stroke-width="4" opacity="0.8"/>
      <line x1="720" y1="0" x2="866" y2="260" stroke="#fff" stroke-width="2" opacity="0.6"/>
      <line x1="650" y1="420" x2="780" y2="640" stroke="#fff" stroke-width="3" opacity="0.6"/>
    </svg>
    <p class="keywords">PRAYER, FASTING, WORSHIP, PROPHECY, REVIVAL</p>
    <div class="badge"><span class="badge-name">QUVELLO</span></div>
    <h1 class="title">
      <span class="line-one">RADIANT HARVEST</span>
      <span class="line-two">GATHERING</span>
    </h1>
    <div class="rule" style="top:811px"></div>
    <section class="details">
      <p class="date">Date : Tuesday July 2nd, 2021</p>
      <p class="time">Time : 11: 00AM - 7: 00PM</p>
      <p class="venue">Bellmore Hotel, 4817 Wexley Avenue, Portland, Maine 04109</p>
      <p class="room">( <b>Room : Tamarind</b> )</p>
    </section>
    <div class="rule" style="top:1034px"></div>
    <p class="tagline">A One Day Prayer Retreat. Jesus Chris is Lord</p>
    <div class="rule" style="top:1098px"></div>
  </main>
</body>
</html>
```